Qorvane Management LLC Business Card

The sample logo was attached for the business Card Design for Traffic Control Company named Qorvane Management LLC. Card design needs to have the company logo and colors match the logo color. It will be nice to show some images of Traffic control signs or cones, even roads closer that math the company services

Target Market(s)

Temporary traffic control. Road closer.

Industry/Entity Type

Construction

Contact Information for Business Card

basic information, name, job title, address, email phone, website

Font styles to use
Serif
Sans Serif

Colors
F0912C
F2A743
F7CA91
FBE8D2
FDF5EE
EE7325
F08F49
F5BC92
FAE3D3
FDF4ED

```html
<!DOCTYPE html>
<html lang="en">
<head>
<meta charset="utf-8">
<title>Qorvane Management LLC – Business Card</title>
<link rel="stylesheet" href="https://fonts.googleapis.com/css2?family=Poppins:wght@400;500;600&display=swap">
<style>
  :root {
    --orange: #f37231;
    --orange-deep: #e0652b;
    --ink: #3a3a3a;
    --card-grey: #e9e9e9;
    --white: #ffffff;
    --backdrop: #dfe3e3;
  }
  * { margin: 0; padding: 0; box-sizing: border-box; }
  html, body {
    width: 1200px; height: 800px; overflow: hidden;
    background: var(--backdrop);
    font-family: "Poppins", sans-serif;
  }
  .canvas { position: relative; width: 1200px; height: 800px; }

  .card {
    position: absolute;
    overflow: hidden;
    box-shadow: 0 2px 6px rgba(0,0,0,.18);
  }

  /* Front side */
  .card-front {
    left: 193px; top: 101px; width: 432px; height: 270px;
    background: linear-gradient(170deg, var(--card-grey) 0%, var(--card-grey) 35%, var(--white) 65%);
  }
  .card-front .swoosh { position: absolute; inset: 0; width: 100%; height: 100%; }
  .holder-name {
    position: absolute; left: 23px; top: 40px;
    font-size: 29px; font-weight: 600; color: var(--ink); letter-spacing: .2px;
  }
  .name-rule { position: absolute; left: 15px; top: 81px; width: 212px; height: 6px; }
  .holder-title {
    position: absolute; left: 23px; top: 90px;
    font-size: 15px; font-weight: 400; color: var(--ink);
  }
  .contact-list {
    position: absolute; left: 20px; top: 164px; list-style: none;
    font-size: 9.5px; color: var(--ink); line-height: 1.2;
  }
  .contact-list li {
    position: relative; padding-left: 12px; margin-bottom: 9px;
  }
  .contact-list li::before {
    content: ""; position: absolute; left: 0; top: 2px;
    width: 4px; height: 10px; background: var(--orange);
  }
  .contact-list li.address { margin-bottom: 0; }
  .front-brand {
    position: absolute; left: 248px; top: 216px;
    font-size: 13px; font-weight: 600; color: var(--orange); line-height: 1.15;
  }

  /* Back side */
  .card-back {
    left: 567px; top: 423px; width: 441px; height: 276px;
    background: var(--orange);
  }
  .lane-marks { position: absolute; inset: 0; width: 100%; height: 100%; }
  .back-brand {
    position: absolute; left: 0; right: 0; top: 104px;
    text-align: center; color: var(--white);
    font-size: 27px; font-weight: 600; line-height: 1.2;
  }
</style>
</head>
<body>
<div class="canvas">

  <section class="card card-front" aria-label="Business card front">
    <svg class="swoosh" viewBox="0 0 432 270" preserveAspectRatio="none" aria-hidden="true">
      <defs>
        <linearGradient id="band" x1="0" y1="0" x2="0" y2="1">
          <stop offset="0" stop-color="#e0652b"/>
          <stop offset=".5" stop-color="#f37231"/>
        </linearGradient>
      </defs>
      <path d="M208,0 H432 V270 H381 C378,180 320,60 208,0 Z" fill="url(#band)"/>
      <path d="M214,5 C320,60 400,150 432,222 V270 H416 C405,180 330,70 214,5 Z" fill="#ffffff"/>
    </svg>

    <h1 class="holder-name">Dana Whitlow</h1>
    <svg class="name-rule" viewBox="0 0 212 6" aria-hidden="true">
      <polygon points="0,0 196,0 193,6 0,6" fill="#f37231"/>
      <polygon points="199,0 203,0 200,6 196,6" fill="#f37231"/>
      <polygon points="206,0 210,0 207,6 203,6" fill="#f37231"/>
    </svg>
    <p class="holder-title">Manager</p>

    <ul class="contact-list">
      <li>+012 34567890</li>
      <li>youremail@mailbox.com</li>
      <li>yourwebsite.com</li>
      <li class="address">your company addres line 1<br>addres line 2</li>
    </ul>

    <p class="front-brand">Qorvane<br>Management LLC</p>
  </section>

  <section class="card card-back" aria-label="Business card back">
    <svg class="lane-marks" viewBox="0 0 441 276" aria-hidden="true">
      <g fill="#ffffff">
        <rect x="32" y="25" width="32" height="9"/>
        <rect x="101" y="25" width="32" height="9"/>
        <rect x="170" y="25" width="32" height="9"/>
        <rect x="239" y="25" width="32" height="9"/>
        <rect x="308" y="25" width="32" height="9"/>
        <rect x="377" y="25" width="32" height="9"/>
        <rect x="32" y="241" width="32" height="9"/>
        <rect x="101" y="241" width="32" height="9"/>
        <rect x="170" y="241" width="32" height="9"/>
        <rect x="239" y="241" width="32" height="9"/>
        <rect x="308" y="241" width="32" height="9"/>
        <rect x="377" y="241" width="32" height="9"/>
      </g>
    </svg>
    <p class="back-brand">Qorvane<br>Management LLC</p>
  </section>

</div>
</body>
</html>
```